Stated Income Loans

Flyer design to be used on social media platforms (i.e. Chatterly, Snapfeed etc.)

Target Market(s)

Real Estate Investors

Requirements
Must have
• INVESTOR STATED INCOME LOANS
• "IT'S TIME TO THINK BIG"
• * Purchase or Refinance up to 3 Million
• * No Income Docs or Bank Statements
• * Vacant Properties Allowed
• * Minimum Credit Score 620
• * Cash Out up to 80%
• Same Day Pre-Approval
• 20-30 Day Close
• Call Marcus Delby today...
• Bluecrest Lending Group, Inc.
• Phone (800) 947-2651 x 17
• Direct (240) 368-9042
• www.bluecrestlendgrp.example
• NMLS #738164 / #50817
Should not have
• Do not use same color scheme as website. Be creative.

```html
<!DOCTYPE html>
<html lang="en">
<head>
<meta charset="utf-8">
<title>Investor Stated Income Loans</title>
<link href="https://fonts.googleapis.com/css2?family=Jost:wght@400;500;600&family=Montserrat:wght@700;800&display=swap" rel="stylesheet">
<style>
  :root {
    --brand-blue: #14506e;
    --brand-blue-deep: #0e3d56;
    --ink: #1d1d1f;
    --paper: #ffffff;
    --paper-soft: #f1f2f4;
  }
  * { margin: 0; padding: 0; box-sizing: border-box; }
  html, body { width: 960px; height: 1200px; overflow: hidden; background: var(--paper); }
  .flyer {
    position: relative; width: 960px; height: 1200px; overflow: hidden;
    background: linear-gradient(160deg, var(--paper) 0%, var(--paper-soft) 55%, var(--paper) 100%);
    font-family: "Jost", sans-serif; color: var(--ink);
  }
  .title-band {
    position: absolute; left: 0; top: 0; width: 960px; height: 101px;
    background: var(--brand-blue);
    display: flex; align-items: center; justify-content: center;
  }
  .title-band h1 {
    font-family: "Montserrat", sans-serif; font-weight: 800; font-size: 40px;
    color: var(--paper); letter-spacing: 1.5px;
  }
  .hero-photo {
    position: absolute; left: 0; top: 101px; width: 960px; height: 403px;
    background:
      radial-gradient(ellipse 260px 200px at 430px 150px, rgba(245,245,245,0.95), rgba(245,245,245,0) 70%),
      radial-gradient(ellipse 220px 260px at 840px 120px, rgba(30,30,30,0.85), rgba(30,30,30,0) 75%),
      radial-gradient(ellipse 300px 200px at 820px 380px, rgba(40,40,40,0.9), rgba(40,40,40,0) 70%),
      linear-gradient(100deg, #3a3a3a 0%, #6e6e6e 22%, #c9c9c9 42%, #dedede 55%, #8a8a8a 72%, #2c2c2c 100%);
  }
  .headline-box {
    position: absolute; left: 0; top: 246px; width: 523px; height: 201px;
    background: rgba(20, 80, 110, 0.86);
    color: var(--paper); padding: 8px 0 0 52px; line-height: 0.95;
  }
  .headline-box .small { font-size: 62px; font-weight: 400; display: block; }
  .headline-box .mid { font-size: 66px; font-weight: 400; display: block; }
  .headline-box .big { font-family: "Montserrat", sans-serif; font-size: 70px; font-weight: 800; display: block; margin-top: 4px; }
  .features { position: absolute; left: 45px; top: 548px; list-style: none; }
  .features li {
    display: flex; align-items: center; height: 46.3px;
    font-size: 27px; font-weight: 400;
  }
  .features svg { width: 30px; height: 30px; margin-right: 28px; flex: none; }
  .features .hl { color: var(--brand-blue); font-weight: 500; }
  .features .hl-lg { color: var(--brand-blue); font-weight: 500; font-size: 37px; line-height: 1; }
  .money-photo { position: absolute; left: 0; top: 0; }
  .contact-band {
    position: absolute; left: 0; top: 972px; width: 960px; height: 121px;
    background: var(--brand-blue);
  }
  .logo-card {
    position: absolute; left: 33px; top: 914px; width: 345px; height: 200px;
    background: var(--paper); box-shadow: 0 4px 14px rgba(0,0,0,0.25);
    display: flex; align-items: center; justify-content: center; gap: 12px;
  }
  .logo-card .mark { width: 22px; height: 22px; border-radius: 50%; background: var(--brand-blue); flex: none; }
  .logo-card .name { font-size: 21px; font-weight: 500; color: var(--brand-blue); line-height: 1.2; }
  .call-line { position: absolute; left: 405px; top: 936px; font-size: 20px; font-weight: 500; }
  .call-line strong { color: var(--brand-blue); font-weight: 600; }
  .contact-details {
    position: absolute; left: 405px; top: 985px; list-style: none;
    color: var(--paper); font-size: 18px; font-weight: 500; line-height: 24.5px;
  }
  .agent-photo {
    position: absolute; left: 679px; top: 892px; width: 269px; height: 201px;
    background:
      radial-gradient(ellipse 60px 80px at 132px 70px, #6b4a38 0%, #4e3629 70%, rgba(78,54,41,0) 100%),
      linear-gradient(180deg, rgba(0,0,0,0) 0%, rgba(0,0,0,0) 52%, #1c1d22 62%, #0f1013 100%);
  }
  .socials {
    position: absolute; left: 0; top: 1142px; width: 960px;
    display: flex; justify-content: center; gap: 26px; list-style: none;
  }
  .socials li {
    display: flex; align-items: center; gap: 7px;
    font-size: 15px; font-weight: 500; color: var(--brand-blue);
  }
  .socials li::before {
    content: ""; width: 12px; height: 12px; border-radius: 50%; border: 2px solid var(--brand-blue);
  }
  .bottom-rule { position: absolute; left: 0; top: 1190px; width: 960px; height: 10px; background: var(--brand-blue); }
</style>
</head>
<body>
<main class="flyer">
  <header class="title-band"><h1>INVESTOR STATED INCOME LOANS</h1></header>

  <div class="hero-photo" role="img" aria-label="Black and white photo looking up at glass skyscrapers against a cloudy sky"></div>
  <div class="headline-box">
    <span class="small">It’s</span>
    <span class="mid">TIME To</span>
    <span class="big">THINK BIG</span>
  </div>

  <svg class="money-photo" width="960" height="1200" viewBox="0 0 960 1200">
    <defs>
      <radialGradient id="moneyTone" cx="0.62" cy="0.5" r="0.7">
        <stop offset="0" stop-color="#b5b5b5"/>
        <stop offset="0.35" stop-color="#6a6a6a"/>
        <stop offset="0.75" stop-color="#2a2a2a"/>
        <stop offset="1" stop-color="#0d0d0d"/>
      </radialGradient>
    </defs>
    <polygon points="668,544 684,544 452,877 436,877" fill="#14506e"/>
    <polygon points="689,544 960,544 960,877 458,877" fill="url(#moneyTone)" role="img" aria-label="Black and white photo of a rolled stack of banknotes beside a calculator and market figures"/>
  </svg>

  <ul class="features">
    <li><svg viewBox="0 0 30 30"><circle cx="13" cy="15" r="11" fill="none" stroke="#14506e" stroke-width="2.4"/><path d="M8 14l5 5 13-14" fill="none" stroke="#14506e" stroke-width="2.8"/></svg>Purchase or Refinance up to&nbsp;<span class="hl-lg">3 Million</span></li>
    <li><svg viewBox="0 0 30 30"><circle cx="13" cy="15" r="11" fill="none" stroke="#14506e" stroke-width="2.4"/><path d="M8 14l5 5 13-14" fill="none" stroke="#14506e" stroke-width="2.8"/></svg><span class="hl">No</span>&nbsp;Income Docs or Bank Statements</li>
    <li><svg viewBox="0 0 30 30"><circle cx="13" cy="15" r="11" fill="none" stroke="#14506e" stroke-width="2.4"/><path d="M8 14l5 5 13-14" fill="none" stroke="#14506e" stroke-width="2.8"/></svg>Vacant Properties Allowed</li>
    <li><svg viewBox="0 0 30 30"><circle cx="13" cy="15" r="11" fill="none" stroke="#14506e" stroke-width="2.4"/><path d="M8 14l5 5 13-14" fill="none" stroke="#14506e" stroke-width="2.8"/></svg>Minimum Credit Score&nbsp;<span class="hl-lg">620</span></li>
    <li><svg viewBox="0 0 30 30"><circle cx="13" cy="15" r="11" fill="none" stroke="#14506e" stroke-width="2.4"/><path d="M8 14l5 5 13-14" fill="none" stroke="#14506e" stroke-width="2.8"/></svg>Cash Out up to&nbsp;<span class="hl-lg">80%</span></li>
    <li><svg viewBox="0 0 30 30"><circle cx="13" cy="15" r="11" fill="none" stroke="#14506e" stroke-width="2.4"/><path d="M8 14l5 5 13-14" fill="none" stroke="#14506e" stroke-width="2.8"/></svg>Same Day&nbsp;<span class="hl">Pre-Approval</span></li>
    <li><svg viewBox="0 0 30 30"><circle cx="13" cy="15" r="11" fill="none" stroke="#14506e" stroke-width="2.4"/><path d="M8 14l5 5 13-14" fill="none" stroke="#14506e" stroke-width="2.8"/></svg><span class="hl-lg">20-30</span>&nbsp;Day Close</li>
  </ul>

  <div class="contact-band"></div>
  <div class="logo-card">
    <span class="mark"></span>
    <span class="name">Bluecrest Lending<br>Group, Inc.</span>
  </div>
  <p class="call-line">Call <strong>Marcus Delby</strong> today...</p>
  <ul class="contact-details">
    <li>Phone: (800) 947-2651 x 17</li>
    <li>Direct: (240) 368-9042</li>
    <li>www.bluecrestlendgrp.example</li>
    <li>NMLS #738164 / #50817</li>
  </ul>
  <div class="agent-photo" role="img" aria-label="Portrait of loan officer Marcus Delby in a dark suit and tie"></div>

  <ul class="socials" aria-label="Social media">
    <li>Chatterly</li>
    <li>Chirpline</li>
    <li>Linkwise</li>
  </ul>
  <div class="bottom-rule"></div>
</main>
</body>
</html>
```